Hal's Remedies Business Card Design Project

I need a business card designed for my pharmacy Hal's Remedies. I would like just the logo on one side, maybe with black background and white lettering. The other side I would also like to include my logo which is attached. Also, please include my name and the following information:
Hal Norwick Owner/Pharm D.
Business address is 7163 N Birch Rd Sioux Falls, SD 57291.
Phone number is 605-318-6027 and fax # is 605-318-6031.
my email address is hal@halsremedies.example.
My website is www.halsremedies.example.
My business hours are Monday-Friday 8am-7 pm. Saturday 8am-12 pm. Sunday Closed.
I would like the design to include my logo colors, black, white, and neon green. Silver may be added as a highlight. Thanks.
Pharmacy
See above in product description

```html
<!DOCTYPE html>
<html lang="en">
<head>
<meta charset="utf-8">
<title>Hal's Remedies – Business Card</title>
<link href="https://fonts.googleapis.com/css2?family=Ubuntu:wght@400;500;700&display=swap" rel="stylesheet">
<style>
  :root {
    --stage: #3b3b3b;
    --stage-light: #4a4a4a;
    --card-white: #f7f7f7;
    --card-black: #121212;
    --ink: #2a2a2a;
    --ink-soft: #555555;
    --neon: #9bc53d;
    --white: #ffffff;
  }
  * { margin: 0; padding: 0; box-sizing: border-box; }
  html, body { width: 1200px; height: 871px; overflow: hidden; }
  body {
    background: radial-gradient(ellipse at 50% 30%, var(--stage-light), var(--stage) 70%);
    font-family: "Ubuntu", sans-serif;
    position: relative;
  }
  .card {
    position: absolute;
    top: 287px;
    width: 520px;
    height: 297px;
    border-radius: 3px;
    box-shadow: 0 14px 30px rgba(0,0,0,0.45);
    overflow: hidden;
  }
  /* Back side */
  .card--info { left: 50px; background: var(--card-white); color: var(--ink); }
  .name-band {
    position: absolute;
    top: 30px; left: 300px;
    width: 240px; height: 50px;
    background: var(--neon);
    border-radius: 25px 0 0 25px;
    color: var(--white);
    padding: 9px 0 0 26px;
  }
  .name-band__name { font-size: 13px; font-weight: 500; letter-spacing: 0.2px; }
  .name-band__role { font-size: 10.5px; margin-top: 3px; }
  .brand {
    position: absolute;
    top: 118px; left: 40px;
    display: flex; align-items: center; gap: 12px;
  }
  .brand__dot { width: 14px; height: 14px; border-radius: 50%; background: var(--neon); }
  .brand__name { font-size: 24px; font-weight: 700; color: var(--ink); letter-spacing: -0.3px; }
  .contact-list {
    position: absolute;
    top: 164px; left: 290px;
    list-style: none;
    font-size: 11.5px; line-height: 19px; color: var(--ink-soft);
  }
  .address-block {
    position: absolute;
    left: 40px; top: 200px;
    font-size: 11.5px; line-height: 17px; color: var(--ink-soft);
  }
  .address-row { display: flex; gap: 10px; align-items: flex-start; margin-bottom: 10px; }
  .address-row svg { flex: none; margin-top: 2px; }
  /* Front side */
  .card--logo { left: 630px; background: linear-gradient(160deg, #1c1c1c, var(--card-black) 60%); }
  .front-brand {
    position: absolute;
    top: 110px; left: 0; width: 100%;
    display: flex; justify-content: center; align-items: center; gap: 14px;
  }
  .front-brand__name { font-size: 40px; font-weight: 500; color: var(--white); letter-spacing: -0.5px; }
  .front-brand__dot { width: 18px; height: 18px; border-radius: 50%; background: var(--neon); }
  .website {
    position: absolute;
    top: 200px; left: 0; width: 100%;
    text-align: center;
    font-size: 15px; color: var(--neon); letter-spacing: 0.3px;
  }
</style>
</head>
<body>
  <section class="card card--info" aria-label="Card back with contact details">
    <div class="name-band">
      <p class="name-band__name">Hal Norwick Owner/Pharm D.</p>
      <p class="name-band__role">Head of Sales Manager</p>
    </div>
    <div class="brand">
      <span class="brand__dot"></span>
      <span class="brand__name">Hal's Remedies</span>
    </div>
    <ul class="contact-list">
      <li>Phone: 605-318-6027</li>
      <li>Fax: 605-318-6031</li>
      <li>Mon–Fri 8am-7 pm. Sat 8am-12 pm.</li>
      <li>Sunday Closed.</li>
    </ul>
    <div class="address-block">
      <div class="address-row">
        <svg width="10" height="14" viewBox="0 0 10 14" aria-hidden="true"><path d="M5 0a5 5 0 0 0-5 5c0 3.5 5 9 5 9s5-5.5 5-9a5 5 0 0 0-5-5z" fill="#9bc53d"/><circle cx="5" cy="5" r="1.8" fill="#f7f7f7"/></svg>
        <p>7163 N Birch Rd Sioux Falls,<br>SD 57291</p>
      </div>
      <div class="address-row">
        <svg width="12" height="9" viewBox="0 0 12 9" aria-hidden="true"><rect x="0.5" y="0.5" width="11" height="8" fill="none" stroke="#9bc53d"/><path d="M0.5 0.5l5.5 4.5 5.5-4.5" fill="none" stroke="#9bc53d"/></svg>
        <p>hal@halsremedies.example</p>
      </div>
    </div>
  </section>

  <section class="card card--logo" aria-label="Card front with brand name">
    <div class="front-brand">
      <span class="front-brand__name">Hal's Remedies</span>
      <span class="front-brand__dot"></span>
    </div>
    <p class="website">www.halsremedies.example</p>
  </section>
</body>
</html>
```